Business Brochure for Mobile Fleet Mechanic Company

Make a brochure for an mobile mechanic company that is a Bi-fold 8.5"Wx11"H. A Bi-fold would have the outside and inside design so it is a total of 4 pages at 8.5"x11". The print is 2-sides 17"Wx11"H that folds down to 8.5"Wx11"H.
Should have photo of mechanic working. Blue in logo is Pantone 284C. Will provide text to be added to approved design.

Contact Information for Business Card

2-sided card using the same design elements and colors as the brochure.

```html
<!DOCTYPE html>
<html lang="en">
<head>
<meta charset="utf-8">
<title>Wrenchline Bi-fold Brochure – Outside</title>
<link href="https://fonts.googleapis.com/css2?family=Montserrat:wght@400;500;600;700&family=Oswald:wght@300;500&display=swap" rel="stylesheet">
<style>
  :root {
    --brand-blue: #5b9de0;
    --deep-blue: #1e4b83;
    --ink: #222428;
    --body-text: #3a3c40;
    --paper: #ffffff;
    --paper-shade: #f8f9fa;
    --band-dark: #1c1d20;
    --stage: #d9dadc;
  }
  * { box-sizing: border-box; margin: 0; padding: 0; }
  html, body { width: 902px; height: 1200px; overflow: hidden; }
  body {
    background: var(--stage);
    font-family: "Montserrat", sans-serif;
    position: relative;
  }
  .spread {
    position: absolute;
    left: 20px; top: 322px;
    width: 862px; height: 556px;
    display: flex;
    box-shadow: 0 10px 30px rgba(0,0,0,.25);
  }
  .panel {
    position: relative;
    width: 431px; height: 556px;
    overflow: hidden;
    background:
      linear-gradient(90deg, rgba(0,0,0,.025), transparent 30%),
      repeating-linear-gradient(115deg, var(--paper) 0 80px, var(--paper-shade) 80px 160px);
  }
  .panel.cover {
    background:
      linear-gradient(90deg, rgba(0,0,0,.03), transparent 12%),
      repeating-linear-gradient(115deg, var(--paper) 0 80px, var(--paper-shade) 80px 160px);
  }

  /* back panel */
  .feature { position: absolute; left: 173px; width: 230px; }
  .feature h3 { font-size: 12.5px; font-weight: 400; color: var(--brand-blue); margin-bottom: 5px; white-space: nowrap; }
  .feature h3 b { font-weight: 600; color: var(--ink); }
  .feature p { font-size: 6.6px; line-height: 1.45; color: var(--body-text); text-align: justify; }
  .photo-strip { position: absolute; top: 319px; left: 0; width: 431px; height: 86px; display: flex; gap: 4px; }
  .photo { height: 100%; }
  .photo.gears { width: 129px; background: linear-gradient(135deg, #6d6f72, #2e3033); }
  .photo.engine { width: 164px; background: linear-gradient(135deg, #7d7a5a, #35383a 70%, #b9a77a); }
  .photo.mechanic { width: 130px; background: linear-gradient(135deg, #c9cdd2, #6d7a8a 60%, #2f4460); }
  .contact-band {
    position: absolute; top: 405px; left: 0; width: 431px; height: 151px;
    background: repeating-linear-gradient(45deg, var(--band-dark) 0 3px, #202124 3px 6px);
  }
  .wordmark { font-weight: 600; color: var(--brand-blue); letter-spacing: -0.5px; white-space: nowrap; }
  .contact-band .wordmark { position: absolute; left: 34px; top: 100px; font-size: 24px; }
  .touch { position: absolute; left: 249px; top: 14px; width: 160px; color: #fff; }
  .touch h4 { font-size: 10px; font-weight: 700; }
  .touch h4 span { color: var(--brand-blue); font-weight: 500; }
  .touch .lead { font-size: 6.6px; line-height: 1.45; color: #d0d2d6; margin: 3px 0 8px; }
  .touch-row { display: flex; align-items: center; gap: 9px; height: 26px; }
  .touch-row svg { flex: none; }
  .touch-row .addr { font-size: 6.6px; color: #d0d2d6; }
  .touch-row .phone { font-size: 9px; font-weight: 700; }
  .touch-row .web { font-size: 6.6px; line-height: 1.35; color: #d0d2d6; }

  /* cover panel */
  .cover-photo {
    position: absolute; left: 209px; top: 0; width: 222px; height: 556px;
    border-radius: 44px 0 0 44px;
    background: linear-gradient(180deg, #123a6e 0%, var(--deep-blue) 40%, #4f6f96 72%, #a7afb9 100%);
  }
  .cover .wordmark { position: absolute; left: 27px; top: 96px; font-size: 30px; }
  .headline-box {
    position: absolute; left: 24px; top: 186px; width: 254px; height: 233px;
    border: 1px solid #9fb9d8;
    padding: 20px 0 0 13px;
  }
  .headline-box h1 { font-family: "Oswald", sans-serif; font-weight: 500; font-size: 33px; line-height: 1.05; color: var(--brand-blue); }
  .headline-box h1 span { display: block; font-weight: 300; color: #6a6d72; }
  .headline-box hr { width: 30px; border: 0; border-top: 1px solid #b8bbbf; margin: 14px 0 12px; }
  .headline-box p { width: 150px; font-size: 6.9px; line-height: 1.45; color: var(--body-text); }
  .tab {
    position: absolute; left: 188px; top: 262px; width: 38px; height: 38px;
    border-radius: 50%; background: var(--deep-blue);
    box-shadow: 0 0 0 6px rgba(255,255,255,.25);
    display: flex; align-items: center; justify-content: center;
  }
  .site { position: absolute; left: 31px; top: 524px; display: flex; align-items: center; gap: 10px; font-size: 7px; letter-spacing: 3px; color: #555; }
</style>
</head>
<body>
  <main class="spread">
    <section class="panel back">
      <article class="feature" style="top:28px">
        <h3>Your Headline 1 <b>Text Goes Here</b></h3>
        <p>Lorem Ipsum is simply dummy text of the printing and typesetting industry. Lorem Ipsum has been the industry's standard dummy text ever since the 1500s, when an unknown printer took a galley of type and scrambled it to make a type specimen book.</p>
      </article>
      <article class="feature" style="top:103px">
        <h3>Your Headline 2 <b>Text Goes Here</b></h3>
        <p>Lorem Ipsum is simply dummy text of the printing and typesetting industry. Lorem Ipsum has been the industry's standard dummy text ever since the 1500s, when an unknown printer took a galley of type and scrambled it to make a type specimen book.</p>
      </article>
      <article class="feature" style="top:176px">
        <h3>Your Headline 3 <b>Text Goes Here</b></h3>
        <p>Lorem Ipsum is simply dummy text of the printing and typesetting industry. Lorem Ipsum has been the industry's standard dummy text ever since the 1500s, when an unknown printer took a galley of type and scrambled it to make a type specimen book.</p>
      </article>
      <article class="feature" style="top:249px">
        <h3>Your Headline 4 <b>Text Goes Here</b></h3>
        <p>Lorem Ipsum is simply dummy text of the printing and typesetting industry. Lorem Ipsum has been the industry's standard dummy text ever since the 1500s, when an unknown printer took a galley of type and scrambled it to make a type specimen book.</p>
      </article>

      <div class="photo-strip">
        <div class="photo gears" role="img" aria-label="Photo of interlocking metal gears"></div>
        <div class="photo engine" role="img" aria-label="Photo of a vehicle engine bay"></div>
        <div class="photo mechanic" role="img" aria-label="Photo of a mechanic working on a car wheel"></div>
      </div>

      <div class="contact-band">
        <div class="wordmark">Wrenchline</div>
        <div class="touch">
          <h4>GET <span>IN TOUCH</span></h4>
          <p class="lead">Lorem Ipsum is simply dummy text of the printing and typesetting industry.</p>
          <div class="touch-row">
            <svg width="16" height="16" viewBox="0 0 16 16"><circle cx="8" cy="8" r="8" fill="#5b9de0"/><path d="M8 3.5a2.6 2.6 0 0 0-2.6 2.6C5.4 8 8 11.5 8 11.5s2.6-3.5 2.6-5.4A2.6 2.6 0 0 0 8 3.5z" fill="#fff"/><circle cx="8" cy="6.1" r="1" fill="#5b9de0"/></svg>
            <span class="addr">Your Address Goes Here</span>
          </div>
          <div class="touch-row">
            <svg width="16" height="16" viewBox="0 0 16 16"><circle cx="8" cy="8" r="8" fill="#5b9de0"/><rect x="5.5" y="3.5" width="5" height="9" rx="1" fill="none" stroke="#fff" stroke-width="1.1"/></svg>
            <span class="phone">0800-24-68-10</span>
          </div>
          <div class="touch-row">
            <svg width="16" height="16" viewBox="0 0 16 16"><circle cx="8" cy="8" r="8" fill="#5b9de0"/><circle cx="8" cy="8" r="4" fill="none" stroke="#fff"/><path d="M4 8h8M8 4c-2 2.5-2 5.5 0 8M8 4c2 2.5 2 5.5 0 8" fill="none" stroke="#fff" stroke-width=".7"/></svg>
            <span class="web">info@yourmailid.com<br>www.yourwebsite.com</span>
          </div>
        </div>
      </div>
    </section>

    <section class="panel cover">
      <div class="cover-photo" role="img" aria-label="Blue-toned photo of a tree-lined road seen on a hand-held phone"></div>
      <div class="wordmark">Wrenchline</div>
      <div class="headline-box">
        <h1>YOUR<br>HEADLINE<span>GOES HERE</span></h1>
        <hr>
        <p>Lorem Ipsum is simply dummy text of the printing and typesetting industry. Lorem Ipsum has been the industry's standard dummy text ever since the 1500s, when an unknown printer took a galley of type and scrambled it to make a type specimen book.</p>
      </div>
      <div class="tab">
        <svg width="10" height="14" viewBox="0 0 10 14"><path d="M7 2 2 7l5 5" fill="none" stroke="#fff" stroke-width="1.5"/></svg>
      </div>
      <div class="site">
        <svg width="13" height="13" viewBox="0 0 16 16"><circle cx="8" cy="8" r="8" fill="#5b9de0"/><circle cx="8" cy="8" r="4" fill="none" stroke="#fff"/><path d="M4 8h8" stroke="#fff" stroke-width=".7"/></svg>
        <span>www.website.com</span>
      </div>
    </section>
  </main>
</body>
</html>
```